Valtrix Inc

Hello.

I would like to take a wordpress ecomm template and turn it into a website that can display 100s of domain listings with short text box for description and a price .
One link to quibblepay.example for immediate payment and with the confirmation/decline letter/email .
Five - six pages, Home, about us, domains, contact us, . Several columns or scrolling page for the domain page. I want to list several hundred virtual domains for sale .
Like a portfolio website but lists domain text .
This will be hosted on my server. On my domain.

Target Market(s)

End users, business owners, store front managers, online entpenauers , ect

Industry/Entity Type

Information Technology

Number of Pages Required

5+ page

Font styles to use
Sans Serif

Colors
0455a3
f78f20
abd036

Requirements
Must have
• Lots of white space, clean professional look . fast loading , use of greens and blues. Easy to read font.
• big headers , several - three different headers that rotate or move or clicks.
• A few current stock photos.
Should not have
• slow loading photos.
• More than two photos on any one page.

```html
<!DOCTYPE html>
<html lang="en">
<head>
<meta charset="utf-8">
<title>Valtrix Domains</title>
<link href="https://fonts.googleapis.com/css2?family=Lato:wght@300;400;700;900&display=swap" rel="stylesheet">
<style>
:root{
  --blue:#0455a3;
  --orange:#f78f20;
  --green:#abd036;
  --dark:#333333;
  --black:#111111;
  --row-alt:#ebebe8;
  --grey-band:#e6e6e6;
  --text:#333333;
  --hero-light:#dde0e6;
  --hero-dark:#b9bec8;
  --social:#5a6478;
}
*{box-sizing:border-box;margin:0;padding:0}
html,body{width:878px;height:1200px;overflow:hidden}
body{font-family:'Lato',sans-serif;color:var(--text);background:#fff;position:relative}
.site-header{position:absolute;left:0;top:0;width:878px;height:94px;background:var(--blue)}
.brand{position:absolute;left:75px;top:28px;display:flex;align-items:center;gap:14px}
.brand-dot{width:58px;height:52px;border-radius:50%;background:var(--orange)}
.brand-name{color:#fff;font-weight:300;font-size:23px;line-height:26px;letter-spacing:.5px}
.utility{position:absolute;left:548px;top:0;width:245px;height:28px;background:#fff;
  clip-path:polygon(0 0,100% 0,94% 100%,6% 100%);display:flex;justify-content:center;align-items:center;font-size:9px;color:#555}
.utility span{padding:0 9px;border-right:1px solid #ddd;line-height:28px}
.utility span:last-child{border:none}
.utility b{color:var(--orange);font-weight:700;margin-right:3px}
.phone{position:absolute;left:448px;top:9px;color:#fff;font-size:12px;display:flex;align-items:center;gap:5px}
.main-nav{position:absolute;top:58px;left:0;width:878px;font-size:13px;color:#fff;letter-spacing:.3px}
.main-nav a{position:absolute;color:#fff;text-decoration:none}
.main-nav .active{font-weight:700;border-bottom:2px solid #fff;padding-bottom:9px}
.hero{position:absolute;left:0;top:94px;width:878px;height:345px;
  background:linear-gradient(160deg,var(--hero-light),var(--hero-dark))}
.hero-title{position:absolute;left:0;top:160px;width:878px;text-align:center;color:#fff;font-weight:900;font-size:21px;letter-spacing:.2px;text-shadow:0 1px 4px rgba(0,0,0,.6)}
.search{position:absolute;left:164px;top:202px;width:550px;height:33px;display:flex}
.search-input{width:327px;background:#fff;display:flex;align-items:center;padding-left:12px;gap:8px;font-size:12px;color:#666}
.search-tld{width:77px;background:#fff;border-left:1px solid #ccc;display:flex;align-items:center;justify-content:space-between;padding:0 10px;font-size:12px;color:var(--blue);font-weight:700}
.search-btn{flex:1;background:var(--orange);color:#fff;font-size:16px;display:flex;align-items:center;justify-content:center}
.welcome h1{position:absolute;top:452px;width:878px;text-align:center;font-weight:300;font-size:22px;color:#222;letter-spacing:.3px}
.welcome h1 em{font-style:normal;color:var(--blue)}
.rule{position:absolute;left:423px;top:490px;width:32px;height:2px;background:var(--blue)}
.welcome p{position:absolute;left:75px;top:502px;width:728px;text-align:center;font-size:9.6px;line-height:18px;color:#333}
.btn-read{position:absolute;left:398px;top:603px;width:83px;height:28px;background:var(--blue);color:#fff;font-size:11px;font-weight:700;display:flex;align-items:center;justify-content:center}
.listings{position:absolute;left:72px;top:653px;width:734px;border-collapse:collapse;border-radius:4px;overflow:hidden;font-size:9.5px;letter-spacing:-.2px}
.listings th{background:var(--green);color:#fff;text-align:left;height:52px;font-size:15px;font-weight:900;letter-spacing:.5px;padding-left:16px;border-left:1px solid #9bbd30}
.listings th:first-child{border:none}
.listings td{height:30.2px;padding-left:16px;border-left:1px solid #ddd;color:#333}
.listings td:first-child{border:none;padding-left:16px}
.listings tr:nth-child(even) td{background:var(--row-alt)}
.listings tr.chosen td{color:var(--blue)}
.listings tr.chosen td.name{font-weight:700}
.box{display:inline-block;width:9px;height:9px;border:1px solid #888;background:#fff;position:relative}
.buy{display:flex;align-items:center;gap:14px}
.buy span{background:#222;color:#fff;font-size:9px;font-weight:700;padding:3px 7px}
.chosen .buy span{background:var(--blue)}
.results-bar{position:absolute;left:72px;top:1007px;width:734px;height:39px;background:var(--dark);border-radius:0 0 4px 4px;color:#fff;font-size:13px;display:flex;align-items:center;justify-content:space-between;padding:0 18px 0 14px}
.pager{display:flex;align-items:center;gap:8px}
.pager i{width:19px;height:19px;background:#fff;display:flex;align-items:center;justify-content:center}
.pager u{text-decoration:none;border-bottom:1px solid #fff}
.cta{position:absolute;left:0;top:1074px;width:878px;height:79px;background:var(--grey-band)}
.cta h2{position:absolute;left:138px;top:20px;font-weight:300;font-size:29px;color:#222;letter-spacing:.3px}
.cta a{position:absolute;left:601px;top:20px;width:136px;height:39px;background:var(--orange);color:#fff;font-size:15px;font-weight:900;display:flex;align-items:center;justify-content:center;text-decoration:none}
.site-footer{position:absolute;left:0;top:1153px;width:878px;height:47px;background:var(--black);color:#fff;font-size:11.5px}
.copy{position:absolute;left:72px;top:16px}
.pay{position:absolute;left:566px;top:11px;width:129px;height:24px;background:#f7c331;border-radius:3px;color:#222;font-size:10px;font-weight:700;display:flex;align-items:center;justify-content:center}
.social{position:absolute;left:708px;top:13px;display:flex;gap:6px}
.social span{width:20px;height:20px;border-radius:50%;background:var(--social)}
</style>
</head>
<body>
<header class="site-header">
  <div class="brand"><div class="brand-dot"></div><div class="brand-name">VALTRIX<br>DOMAINS</div></div>
  <div class="phone"><svg width="11" height="11" viewBox="0 0 24 24"><path fill="#f78f20" d="M6.6 10.8a15 15 0 0 0 6.6 6.6l2.2-2.2a1 1 0 0 1 1-.3 11 11 0 0 0 3.6.6 1 1 0 0 1 1 1V20a1 1 0 0 1-1 1A17 17 0 0 1 3 4a1 1 0 0 1 1-1h3.5a1 1 0 0 1 1 1 11 11 0 0 0 .6 3.6 1 1 0 0 1-.3 1z"/></svg>555-014-2290</div>
  <div class="utility"><span><b>♥</b>Wish List</span><span><b>▪</b>Log In</span><span><b>●</b>My Account</span></div>
  <nav class="main-nav">
    <a class="active" style="left:452px">HOME</a>
    <a style="left:523px">ABOUT US</a>
    <a style="left:619px">DOMAINS</a>
    <a style="left:718px">CONTACT US</a>
  </nav>
</header>

<section class="hero" role="img" aria-label="Hero photo: glossy spheres labelled with domain endings">
  <h2 class="hero-title">FIND A GREAT DOMAIN AT THE BEST PRICES</h2>
  <div class="search">
    <div class="search-input"><svg width="13" height="13" viewBox="0 0 24 24"><circle cx="10" cy="10" r="6.5" fill="none" stroke="#0455a3" stroke-width="3"/><path d="M15 15l6 6" stroke="#0455a3" stroke-width="3.5"/></svg>Search Domain Name</div>
    <div class="search-tld">.com<svg width="10" height="6" viewBox="0 0 10 6"><path d="M1 1l4 4 4-4" fill="none" stroke="#333"/></svg></div>
    <div class="search-btn">Check Availability</div>
  </div>
</section>

<section class="welcome">
  <h1>WELCOME TO <em>VALTRIX DOMAINS</em></h1>
  <div class="rule"></div>
  <p>Donec accumsan mollis efficitur. Vestibulum ante ipsum primis in faucibus orci luctus et ultrices posuere cubilia Curae; Donec a lectus sit amet nisl hendrerit convallis. Nam tincidunt euismod nisi vitae lacinia. Quisque faucibus nisi sed iaculis sodales. Donec venenatis a ligula efficitur viverra. Duis ultrices bibendum metus eu aliquam. Pellentesque habitant morbi tristique senectus et netus et malesuada fames ac turpis egestas. Phasellus eget sem vitae diam euismod commodo. Fusce in condimentum nibh. Ut sollicitudin sed ligula quis ultrices. Nullam id tortor sed justo luctus placerat. Curabitur malesuada justo at enim commodo, id ultrices arcu lobortis. In vitae viverra lectus. Sed et vestibulum lorem.</p>
  <div class="btn-read">Read More »</div>
</section>

<svg width="0" height="0" style="position:absolute">
  <symbol id="cart" viewBox="0 0 28 18"><path d="M1 2h4l3 10h13l3-7H7" fill="none" stroke="currentColor" stroke-width="1.6"/><circle cx="10" cy="15" r="1.8" fill="none" stroke="currentColor" stroke-width="1.4"/><circle cx="22" cy="12" r="4" fill="none" stroke="currentColor" stroke-width="1.4"/><path d="M22 10v4M20 12h4" stroke="currentColor" stroke-width="1.2"/></symbol>
</svg>

<table class="listings">
  <thead><tr><th style="width:40px"></th><th style="width:171px">DOMAIN NAME</th><th style="width:324px">DESCRIPTION</th><th style="width:74px">PRICE</th><th>BUY NOW</th></tr></thead>
  <tbody>
    <tr class="chosen"><td><span class="box"><svg width="14" height="10" viewBox="0 0 14 10" style="position:absolute;left:-1px;top:-3px"><path d="M1 5l4 4 8-8" fill="none" stroke="#0455a3" stroke-width="1.8"/></svg></span></td><td class="name">loremipsum.com</td><td>Lorem ipsum dolor sit amet, consectetur adipiscing elit suscipit</td><td>$40.35</td><td><div class="buy"><svg width="24" height="16" style="color:#0455a3"><use href="#cart"/></svg><span>Buy Now</span></div></td></tr>
    <tr><td><span class="box"></span></td><td>adipiscingelitsuscipit.com</td><td>Lorem ipsum dolor sit amet, consectetur adipiscing</td><td>$10.35</td><td><div class="buy"><svg width="24" height="16" style="color:#f78f20"><use href="#cart"/></svg><span>Buy Now</span></div></td></tr>
    <tr><td><span class="box"></span></td><td>abcdefghijklmnopqrstuvwxyz.com</td><td>Lorem ipsum dolor sit amet, consectetur adipiscing elit susc</td><td>$80.35</td><td><div class="buy"><svg width="24" height="16" style="color:#f78f20"><use href="#cart"/></svg><span>Buy Now</span></div></td></tr>
    <tr><td><span class="box"></span></td><td>loremipsum.com</td><td>Lorem ipsum dolor sit amet, consectetur adipiscing elit suscipit urna ipsum</td><td>$8.55</td><td><div class="buy"><svg width="24" height="16" style="color:#f78f20"><use href="#cart"/></svg><span>Buy Now</span></div></td></tr>
    <tr><td><span class="box"></span></td><td>adipiscingelitsuscipit.com</td><td>Lorem ipsum dolor sit amet, consectetur adipis</td><td>$110.35</td><td><div class="buy"><svg width="24" height="16" style="color:#f78f20"><use href="#cart"/></svg><span>Buy Now</span></div></td></tr>
    <tr><td><span class="box"></span></td><td>abcdefghijklmnopqrstuvwxyz.com</td><td>Lorem ipsum dolor sit amet, consectetur adipiscing elit suscipit</td><td>$40.35</td><td><div class="buy"><svg width="24" height="16" style="color:#f78f20"><use href="#cart"/></svg><span>Buy Now</span></div></td></tr>
    <tr><td><span class="box"></span></td><td>loremipsum.com</td><td>Lorem ipsum dolor sit amet, consectetur adipiscing</td><td>$10.35</td><td><div class="buy"><svg width="24" height="16" style="color:#f78f20"><use href="#cart"/></svg><span>Buy Now</span></div></td></tr>
    <tr><td><span class="box"></span></td><td>adipiscingelitsuscipit.com</td><td>Lorem ipsum dolor sit amet, consectetur adipiscing elit susc</td><td>$80.35</td><td><div class="buy"><svg width="24" height="16" style="color:#f78f20"><use href="#cart"/></svg><span>Buy Now</span></div></td></tr>
    <tr><td><span class="box"></span></td><td>abcdefghijklmnopqrstuvwxyz.com</td><td>Lorem ipsum dolor sit amet, consectetur adipiscing elit suscipit urna ipsum</td><td>$8.55</td><td><div class="buy"><svg width="24" height="16" style="color:#f78f20"><use href="#cart"/></svg><span>Buy Now</span></div></td></tr>
    <tr><td><span class="box"></span></td><td>loremipsum.com</td><td>Lorem ipsum dolor sit amet, consectetur adipis</td><td>$110.35</td><td><div class="buy"><svg width="24" height="16" style="color:#f78f20"><use href="#cart"/></svg><span>Buy Now</span></div></td></tr>
  </tbody>
</table>
<div class="results-bar"><span>47833 Results</span><div class="pager"><i><svg width="8" height="12" viewBox="0 0 8 12"><path d="M1 1l5 5-5 5" fill="none" stroke="#222" stroke-width="1.5"/></svg></i>Page 1 of <u>455</u></div></div>

<section class="cta"><h2>Find Your Perfect Domain Name</h2><a>GET STARTED</a></section>

<footer class="site-footer">
  <div class="copy">Copyright © 2016 Valtrix Domains.All Rights Reserved.</div>
  <div class="pay">Check out with QuibblePay</div>
  <div class="social"><span aria-label="Social link"></span><span aria-label="Social link"></span><span aria-label="Social link"></span><span aria-label="Social link"></span></div>
</footer>
</body>
</html>
```